Biz Card for Harrowfield Property Partners - HWPP

Harrowfield Property Partners is a commercial real estate acquisitions firm. We buy commercial property and need to raise capital from investors for each deal we buy. The vibe needs to be: give us your money, we will multiply it.
Our website: www.hrwpp-example.com
Competitors are: https://velmarholdings-example.com/, https://tribanquepartners-example.com/, http://www.ostrellecapital-example.com/
Target Market(s)
High Net Worth Individuals, Bankers, Insurance Companies, Commercial Real Estate Brokers.
Industry/Entity Type
Investment Banking
Contact Information for Business Card
Name, Title, Addess, Cell#, Office#, email, website
Requirements
Must have
- use one of our logos. See website for look and feel: www.hrwpp-example.com
Nice to have
- see website: www.hrwpp-example.com

```html
<!DOCTYPE html>
<html lang="en">
<head>
<meta charset="utf-8">
<title>Harrowfield Property Partners – Business Card</title>
<link href="https://fonts.googleapis.com/css2?family=Arimo:wght@400;700&display=swap" rel="stylesheet">
<style>
  :root {
    --stage: #3b3532;
    --card-light: #ffffff;
    --card-dark: #1b1b1b;
    --navy: #14324a;
    --ink: #1a2a3a;
    --white: #ffffff;
  }
  * { box-sizing: border-box; margin: 0; padding: 0; }
  html, body {
    width: 1200px; height: 769px; overflow: hidden;
    background: var(--stage);
    font-family: "Arimo", Arial, sans-serif;
  }
  .stage { position: relative; width: 1200px; height: 769px; }
  .card {
    position: absolute; top: 236px;
    width: 520px; height: 297px;
    border-radius: 4px;
  }
  .card--front { left: 60px; background: var(--card-light); color: var(--ink); }
  .card--back { left: 620px; background: var(--card-dark); color: var(--white); }

  .brand-circle { position: absolute; border-radius: 50%; }
  .card--front .brand-circle { left: 34px; top: 30px; width: 76px; height: 76px; background: var(--navy); }
  .card--back .brand-circle { left: 44px; top: 92px; width: 112px; height: 112px; background: var(--white); }

  .brand-name {
    position: absolute;
    font-weight: 400;
    text-transform: uppercase;
    letter-spacing: 0.18em;
    line-height: 1.3;
  }
  .card--front .brand-name { left: 34px; top: 114px; font-size: 19px; color: var(--navy); }
  .card--back .brand-name { left: 176px; top: 118px; font-size: 22px; color: var(--white); }

  .divider {
    position: absolute; left: 34px; right: 30px; top: 172px;
    height: 1.5px; background: var(--navy);
  }
  .address {
    position: absolute; right: 30px; top: 134px;
    text-align: right; font-size: 11px; line-height: 1.35; color: var(--navy);
  }
  .person { position: absolute; left: 44px; top: 182px; }
  .person__name { font-size: 18px; font-weight: 700; color: var(--ink); }
  .person__title { font-size: 12px; color: var(--ink); margin-top: 1px; }

  .contact { position: absolute; left: 44px; top: 228px; list-style: none; }
  .contact__row {
    display: flex; align-items: center; gap: 10px;
    font-size: 12px; color: var(--ink); height: 19px;
  }
  .contact__icon { width: 12px; height: 12px; fill: none; stroke: var(--ink); stroke-width: 1.4; }
</style>
</head>
<body>
<main class="stage">

  <section class="card card--front" aria-label="Business card front">
    <span class="brand-circle" aria-hidden="true"></span>
    <p class="brand-name">Harrowfield<br>Property Partners</p>
    <p class="address">48 Larkspur Ave, Suite 900<br>Westbrook, FL 30000</p>
    <span class="divider" aria-hidden="true"></span>
    <div class="person">
      <p class="person__name">Marcus Ellery</p>
      <p class="person__title">President</p>
    </div>
    <ul class="contact">
      <li class="contact__row">
        <svg class="contact__icon" viewBox="0 0 12 12" aria-hidden="true"><path d="M2 1.5 L4 1.5 L5 4 L3.8 5 Q5 7.5 7 8.2 L8 7 L10.5 8 L10.5 10 Q6 11 3 7.5 Q1 5 2 1.5 Z"/></svg>
        <span>(555) 014-2736</span>
      </li>
      <li class="contact__row">
        <svg class="contact__icon" viewBox="0 0 12 12" aria-hidden="true"><rect x="1" y="2.5" width="10" height="7"/><path d="M1 2.5 L6 6.5 L11 2.5"/></svg>
        <span>info@hrwpp-example.com</span>
      </li>
      <li class="contact__row">
        <svg class="contact__icon" viewBox="0 0 12 12" aria-hidden="true"><circle cx="6" cy="6" r="5"/><path d="M1 6 H11 M6 1 V11 M6 1 Q3 6 6 11 M6 1 Q9 6 6 11"/></svg>
        <span>www.hrwpp-example.com</span>
      </li>
    </ul>
  </section>

  <section class="card card--back" aria-label="Business card back">
    <span class="brand-circle" aria-hidden="true"></span>
    <p class="brand-name">Harrowfield<br>Property Partners</p>
  </section>

</main>
</body>
</html>
```